Front book cover for a training course to help bakers get higher prices and sell more wedding cakes.

We need a front cover for a book that will be teaching bakers how to sell wedding cakes to get higher prices and book more orders. It is a business book. Do not make it look like we want brides to read it. Bakers will be judging the cover to see if it is worth their investment to read it. The title is already in the logo, so do not repeat it.

Target Market(s)

Bakers who sell wedding cakes

Industry/Entity Type

Bakery

Colors

Designer to choose colors to be used in the design.

Requirements
Must have
• Must use the logo. Must have author name: Lou Brand. Must have subtitle: Boost Your Prices. Book More Brides. Build Your Empire.
Nice to have
• You are free to be creative. The concept is not to be pretty. It is a business sales and marketing book

```html
<!DOCTYPE html>
<html lang="en">
<head>
<meta charset="utf-8">
<title>Tiered Profit Coach – Book Cover</title>
<link rel="stylesheet" href="https://fonts.googleapis.com/css2?family=Oswald:wght@500;600;700&display=swap">
<style>
  :root {
    --navy-top: #1b3853;
    --navy-bottom: #1f5076;
    --cream: #d9d0c3;
    --crimson: #d4375b;
    --gold: #f8c400;
  }
  html, body {
    margin: 0;
    padding: 0;
    overflow: hidden;
    background: var(--navy-top);
  }
  .cover {
    position: relative;
    width: 848px;
    height: 1200px;
    overflow: hidden;
    background: linear-gradient(180deg, var(--navy-top) 0%, #1c3f5e 55%, var(--navy-bottom) 100%);
    font-family: "Oswald", "Arial Narrow", sans-serif;
  }
  .brand {
    position: absolute;
    top: 120px;
    left: 0;
    width: 100%;
    text-align: center;
  }
  .brand-dot {
    display: block;
    width: 150px;
    height: 150px;
    margin: 0 auto 70px;
    border-radius: 50%;
    background: var(--crimson);
  }
  .brand-name {
    margin: 0;
    font-weight: 600;
    font-size: 86px;
    line-height: 1;
    color: var(--cream);
    letter-spacing: 1px;
  }
  .subtitle {
    position: absolute;
    top: 535px;
    left: 0;
    width: 100%;
    margin: 0;
    text-align: center;
    font-weight: 700;
    font-size: 60px;
    line-height: 78px;
    color: var(--gold);
    text-transform: uppercase;
    letter-spacing: 0.5px;
  }
  .author {
    position: absolute;
    top: 975px;
    left: 0;
    width: 100%;
    margin: 0;
    text-align: center;
    font-weight: 500;
    font-size: 132px;
    line-height: 1;
    color: var(--cream);
    letter-spacing: 10px;
    text-transform: uppercase;
  }
</style>
</head>
<body>
  <main class="cover">
    <header class="brand">
      <span class="brand-dot" aria-hidden="true"></span>
      <h1 class="brand-name">Tiered Profit Coach</h1>
    </header>
    <p class="subtitle">Boost your prices.<br>Book more brides.<br>Build your empire.</p>
    <p class="author">Lou Brand</p>
  </main>
</body>
</html>
```